Teachers workshop flyer

I need a flyer to inform schools of a workshop for teachers that empowers the teacher to help traumatised and disadvantaged students to engage in successful learning.

I am a teacher and educator and my info for the flyer is attached.

Target Market(s)

Principals and vice-principals who have stressed staff and students and they want things to be better in the school!

Industry/Entity Type

Teacher

```html
<!DOCTYPE html>
<html lang="en">
<head>
<meta charset="utf-8">
<title>Brain-based Strategies for Student Success</title>
<link rel="stylesheet" href="https://fonts.googleapis.com/css2?family=Alfa+Slab+One&family=Carlito:ital,wght@0,400;0,700;1,400;1,700&display=swap">
<style>
  :root {
    --blue: #1f93e3;
    --blue-deep: #0a6fc4;
    --blue-light: #5ab8f5;
    --ink: #1a1a1a;
    --footer: #232323;
    --quote-grey: #8a8a8a;
    --paper-top: #ffffff;
    --paper-bottom: #e4e4e4;
    --photo-dark: #2f4a3e;
    --photo-mid: #5d7a68;
    --photo-light: #c9d2cc;
  }
  * { box-sizing: border-box; margin: 0; padding: 0; }
  html, body { width: 846px; height: 1200px; overflow: hidden; background: #fff; }
  .flyer {
    position: relative; width: 846px; height: 1200px; overflow: hidden;
    font-family: "Carlito", "Calibri", sans-serif; color: var(--ink);
    background: linear-gradient(180deg, var(--paper-top) 560px, var(--paper-top) 780px, var(--paper-bottom) 1094px);
  }
  .hero-photo {
    position: absolute; left: 0; top: 0; width: 846px; height: 564px;
    background:
      linear-gradient(90deg, rgba(0,0,0,0.35) 0%, rgba(0,0,0,0) 30%, rgba(0,0,0,0) 75%, rgba(255,255,255,0.35) 100%),
      linear-gradient(180deg, var(--photo-dark) 0%, var(--photo-mid) 55%, var(--photo-light) 100%);
  }
  .title {
    position: absolute; left: 50px; top: 418px;
    font-family: "Alfa Slab One", serif; font-size: 57px; line-height: 64px;
    color: var(--blue);
    -webkit-text-stroke: 2px #fff; paint-order: stroke fill;
    text-shadow: 0 0 4px #fff, 2px 3px 6px rgba(0,0,0,0.45);
    letter-spacing: 0.5px;
  }
  .intro {
    position: absolute; left: 48px; width: 752px;
    font-size: 15.2px; line-height: 21.5px;
  }
  .intro--one { top: 586px; }
  .intro--two { top: 660px; }
  .presenter {
    position: absolute; left: 40px; top: 734px; width: 772px; height: 130px;
    background: var(--blue); border-radius: 12px;
    box-shadow: 2px 4px 6px rgba(0,0,0,0.35);
    color: #fff; padding: 8px 14px 0 14px;
  }
  .presenter__heading { font-style: italic; font-weight: 700; font-size: 16px; margin-bottom: 4px; }
  .presenter__bio { font-style: italic; font-weight: 700; font-size: 14.6px; line-height: 20px; }
  .quote-mark {
    position: absolute; font-family: "Alfa Slab One", serif; font-size: 170px; line-height: 1;
    color: var(--quote-grey);
  }
  .quote-mark--open { left: 36px; top: 868px; }
  .quote-mark--close { left: 740px; top: 868px; }
  .feedback { position: absolute; left: 77px; top: 884px; width: 720px; font-weight: 700; font-size: 15.6px; line-height: 21px; }
  .feedback__heading { margin-bottom: 8px; }
  .moments-tag {
    position: absolute; left: 53px; top: 974px; width: 236px; height: 24px;
    background: var(--blue); border-radius: 12px; color: #fff;
    font-weight: 700; font-size: 17px; line-height: 24px; padding-left: 20px;
  }
  .moments { position: absolute; left: 70px; top: 1004px; list-style: none; }
  .moments li { font-weight: 700; font-size: 17.4px; line-height: 31.5px; padding-left: 16px; position: relative; }
  .moments li::before {
    content: ""; position: absolute; left: 0; top: 12px; width: 9px; height: 9px;
    border-radius: 50%; background: var(--blue);
  }
  .contact {
    position: absolute; left: 0; top: 1094px; width: 846px; height: 106px;
    background: var(--footer); text-align: center; color: #fff; padding-top: 8px;
  }
  .contact__phone { color: var(--blue); font-weight: 700; font-size: 21px; line-height: 26px; }
  .contact__note { font-weight: 700; font-size: 15px; line-height: 22px; }
  .contact__web { color: var(--blue); font-weight: 700; font-size: 23px; line-height: 28px; }
</style>
</head>
<body>
<main class="flyer">
  <div class="hero-photo" role="img" aria-label="Photo of a teacher and students working through equations at a classroom chalkboard"></div>
  <h1 class="title">Brain-based Strategies<br>for Student Success</h1>

  <p class="intro intro--one">Contemporary teaching is a highly complex role as increasing numbers of students attend school without the essential ‘self-skills’ to be truly ‘school-ready’ and successful. Instead these students often seek-out attention in ways that can disruptive in the classroom causing stress and frustration for teachers.</p>
  <p class="intro intro--two">Dan shows how and why the most effective strategies for these students are guided by a sound understanding of child-development and brain-development - especially where trauma has left lasting impacts. Teachers can learn how to build a student’s self-skills, without the teacher having to become a therapist!</p>

  <section class="presenter">
    <h2 class="presenter__heading">About the Presenter:</h2>
    <p class="presenter__bio">Daniel Whitford is a Melbourne-based therapist and educator with over twenty years experience working with adults and young people in the area of trauma and recovery. Dan’s seminars are engaging and practical since teachers need effective strategies that will immediately translate into classroom practice. Dan has trained here and overseas in the most effective behavior change strategies.</p>
  </section>

  <span class="quote-mark quote-mark--open" aria-hidden="true">“</span>
  <span class="quote-mark quote-mark--close" aria-hidden="true">”</span>
  <blockquote class="feedback">
    <p class="feedback__heading">Teacher Feedback:</p>
    <p>Dan was such an engaging and energetic presenter whom I enjoyed immensely. His presentation on the brain and take away strategies were so practical and meaningful. It was an invaluable session.</p>
  </blockquote>

  <div class="moments-tag">My Light-bulb moments:</div>
  <ul class="moments">
    <li>I need to CONNECT – not correct – far more often.</li>
    <li>Seeing negative self-talk for what it is.</li>
    <li>Using far more ‘diversions’ in the avoidance loop.”</li>
  </ul>

  <footer class="contact">
    <p class="contact__phone">Call 0400 318 552</p>
    <p class="contact__note">for more information or to book Dan to come to your school:</p>
    <p class="contact__web">www.danielwhitford.com.au/studentsuccess</p>
  </footer>
</main>
</body>
</html>
```